Memorial page to show case the life and works of an individual who has passed

I would like to design a website as a memorial page for my mother. She was a very senior member of the London community and would like to design something that has a page for her biography. Gallery. Testimonials. Etc. Something that is smart and modern.
similar to
http://www.gervaldquinnstudio.org/
Not to have things that are flowery it need to be a website that is smart clean and proffesional to showcase the life and works of an indiviudal

there wont be a logo as it is not a company

Industry/Entity Type

Community

Number of Pages Required

4 page

Colors
9bcb3c
abd036
ffffff
f78f20
3176b5

Requirements
Must have
• Gallary
• moving gallary at the top
• About
• Testimonials
• Videos
• Leave a message

```html
<!DOCTYPE html>
<html lang="en">
<head>
<meta charset="utf-8">
<title>Evermore Remembrance — Memorial Page</title>
<link href="https://fonts.googleapis.com/css2?family=Cinzel:wght@400;700&family=Roboto:wght@400;500&display=swap" rel="stylesheet">
<style>
:root{
  --green:#9bcb3c;
  --green-soft:#abd036;
  --white:#ffffff;
  --orange:#f78f20;
  --blue:#3176b5;
  --navy:#2d4a9c;
  --black:#111111;
  --grey-bg:#f4f4f4;
  --text:#555555;
  --line:#c9c9c9;
}
*{margin:0;padding:0;box-sizing:border-box}
html,body{width:1200px;height:3482px;overflow:hidden;background:var(--white)}
body{position:relative;font-family:'Roboto',Arial,sans-serif;color:var(--text)}
.abs{position:absolute}
.heading{font-family:'Cinzel',Georgia,serif;color:var(--blue);font-weight:700;font-size:36px;text-align:center;position:absolute;left:0;width:1200px;letter-spacing:1px}
.heading-mark{position:absolute;width:24px;height:24px}
.heading-mark.tr{border-top:3px solid var(--blue);border-right:3px solid var(--blue);opacity:.6}
.heading-mark.bl{border-bottom:3px solid var(--blue);border-left:3px solid var(--blue);opacity:.6}
.btn{position:absolute;display:flex;align-items:center;justify-content:center;color:var(--white);font-size:17px;border-radius:2px}
.btn-orange{background:var(--orange);box-shadow:0 4px 0 #d9761a}

/* header */
.site-header{position:absolute;left:0;top:0;width:1200px;height:132px;background:linear-gradient(135deg,#2a4796,#3453a8 50%,#2a4796)}
.brand{position:absolute;left:0;top:40px;width:1200px;text-align:center;font-family:'Cinzel',Georgia,serif;color:var(--orange);font-size:22px;line-height:28px}
.brand-dot{position:absolute;left:382px;top:46px;width:26px;height:26px;border-radius:50%;background:var(--orange)}
.main-nav{position:absolute;left:0;top:132px;width:1200px;height:49px;background:var(--black)}
.main-nav .active{position:absolute;left:204px;top:0;width:121px;height:49px;background:var(--green)}
.nav-item{position:absolute;top:0;height:49px;line-height:49px;font-family:'Cinzel',Georgia,serif;font-size:13px;color:var(--white);transform:translateX(-50%)}

/* hero */
.hero{position:absolute;left:0;top:181px;width:1200px;height:480px}
.hero-photo{position:absolute;left:0;top:0;width:1200px;height:480px;background:linear-gradient(90deg,#c9a894 0%,#d8c0b0 25%,#b8c98a 45%,#9bcb3c 70%,#8fc030 100%)}
.hero-title{position:absolute;left:560px;top:120px;width:600px;text-align:center;font-family:'Cinzel',Georgia,serif;color:var(--orange);font-size:29px;line-height:46px}
.hero-sub{position:absolute;left:560px;top:228px;width:600px;text-align:center;color:var(--white);font-size:19px;line-height:35px}
.hero-btn{left:757px;top:316px;width:139px;height:51px;background:#2a5fb5;font-size:18px}
.hero-arrow{position:absolute;top:225px;width:40px;height:40px}
.hero-base{position:absolute;left:88px;top:439px;width:1026px;height:41px;background:var(--white)}

/* gallery */
.gallery-bg{position:absolute;left:0;top:1000px;width:1200px;height:720px;background:radial-gradient(ellipse at 20% 45%,rgba(196,176,226,.45),rgba(255,255,255,0) 55%),radial-gradient(ellipse at 55% 80%,rgba(206,190,232,.35),rgba(255,255,255,0) 50%)}
.gallery-intro{position:absolute;left:149px;top:766px;width:740px;font-size:14px;line-height:27px;color:#666}
.gallery-nav{position:absolute;top:775px;width:30px;height:35px;background:#555}
.tile{position:absolute;width:288px;height:286px}
.tile-caption{position:absolute;width:288px;text-align:center;font-family:'Cinzel',Georgia,serif;color:var(--green);font-size:16px}
.tile-meta{position:absolute;width:288px;text-align:center;font-size:9px;color:var(--green);letter-spacing:1px}

/* about */
.about{position:absolute;left:0;top:1738px;width:1200px;height:479px}
.about-panel{position:absolute;left:0;top:0;width:587px;height:479px;background:var(--green)}
.about-photo{position:absolute;left:587px;top:0;width:613px;height:479px;background:linear-gradient(160deg,#3c4c9a,#5a6a3c 60%,#404d8a)}
.about-title{position:absolute;left:0;top:50px;width:587px;text-align:center;font-family:'Cinzel',Georgia,serif;color:var(--white);font-size:34px;font-weight:700}
.about-text{position:absolute;left:128px;top:156px;width:442px;color:var(--white);font-size:11.5px;line-height:23px;text-align:justify}
.video{position:absolute;left:610px;top:93px;width:516px;height:297px;border:2px solid #dcdcdc}
.video-frame{position:absolute;inset:0;background:linear-gradient(180deg,#2a3040,#4a3a30 60%,#2a2a2a)}
.video-bar{position:absolute;left:0;bottom:0;width:100%;height:26px;background:rgba(20,20,20,.85)}

/* testimonials */
.testimonials{position:absolute;left:0;top:2217px;width:1200px;height:494px;background:var(--grey-bg)}
.avatar{position:absolute;left:534px;top:141px;width:134px;height:134px;border-radius:50%;background:linear-gradient(180deg,#8a6a58,#c0907a)}
.quote{position:absolute;left:150px;top:300px;width:900px;text-align:center;font-size:27px;line-height:36px;color:#555}
.quote-name{position:absolute;left:0;top:392px;width:1200px;text-align:center;font-family:'Cinzel',Georgia,serif;color:var(--green);font-size:15px}
.dots{position:absolute;left:558px;top:445px;display:flex;gap:4px}
.dots span{width:9px;height:9px;border-radius:50%;border:1px solid #bbb}
.dots .on{background:var(--orange);border-color:var(--orange)}

/* contact */
.field{position:absolute;left:153px;width:420px;border:1px solid #aaa;padding:0 22px;font-size:17px;color:#555;display:flex;align-items:center}
.field.area{align-items:flex-start;padding-top:16px}
.contact-text{position:absolute;left:636px;top:2888px;width:400px;font-size:17px;line-height:26px;color:#333}
.contact-addr{position:absolute;left:636px;font-family:'Cinzel',Georgia,serif;font-size:17px;line-height:31px;color:#333}
.social{position:absolute;top:3238px;width:60px;height:60px;border-radius:50%;border:1px solid #999}

.site-footer{position:absolute;left:0;top:3426px;width:1200px;height:56px;background:var(--black);color:#ddd;font-size:14px;text-align:center;line-height:56px}
</style>
</head>
<body>

<header class="site-header">
  <span class="brand-dot"></span>
  <div class="brand">Evermore Remembrance<br>Clara Whitfield</div>
</header>
<nav class="main-nav">
  <span class="active"></span>
  <span class="nav-item" style="left:263px">Home</span>
  <span class="nav-item" style="left:378px">Gallery</span>
  <span class="nav-item" style="left:504px">About Us</span>
  <span class="nav-item" style="left:643px">Testimonials</span>
  <span class="nav-item" style="left:773px">Videos</span>
  <span class="nav-item" style="left:903px">Contact Us</span>
</nav>

<section class="hero">
  <div class="hero-photo" role="img" aria-label="Portrait photograph of an elderly woman smiling, fading into a green backdrop"></div>
  <svg class="hero-arrow" style="left:87px" viewBox="0 0 40 40"><circle cx="20" cy="20" r="17" fill="none" stroke="#555" stroke-width="3"/><path d="M23 12 L15 20 L23 28" fill="none" stroke="#555" stroke-width="3"/></svg>
  <svg class="hero-arrow" style="left:1071px" viewBox="0 0 40 40"><circle cx="20" cy="20" r="17" fill="none" stroke="#444" stroke-width="3"/><path d="M17 12 L25 20 L17 28" fill="none" stroke="#444" stroke-width="3"/></svg>
  <div class="hero-title">Welcome to my mother's<br>memorial page</div>
  <div class="hero-sub">She was a very senior member of the<br>London community</div>
  <div class="btn hero-btn">Learn more</div>
  <div class="hero-base"></div>
</section>

<section class="gallery">
  <div class="gallery-bg" role="img" aria-label="Faint background photograph of lavender flower petals"></div>
  <span class="heading-mark tr" style="left:704px;top:643px"></span>
  <h2 class="heading" style="top:664px">Gallery</h2>
  <span class="heading-mark bl" style="left:470px;top:710px"></span>
  <p class="gallery-intro">Lorem Ipsum is simply dummy text of the printing and typesetting industry. Lorem Ipsum has been the industry's standard dummy text ever since the 1500s, when an .</p>
  <svg class="gallery-nav" style="left:986px" viewBox="0 0 30 35"><rect width="30" height="35" fill="#555"/><path d="M20 17 H8 M13 11 L7 17 L13 23" stroke="#fff" stroke-width="3" fill="none"/></svg>
  <svg class="gallery-nav" style="left:1019px" viewBox="0 0 30 35"><rect width="30" height="35" fill="#555"/><path d="M10 17 H22 M17 11 L23 17 L17 23" stroke="#fff" stroke-width="3" fill="none"/></svg>

  <div class="tile" style="left:149px;top:856px;background:linear-gradient(135deg,#5a3a34,#b83a40 55%,#6a8a3a)" role="img" aria-label="Photograph of a casket with red roses"></div>
  <div class="tile" style="left:455px;top:856px;background:linear-gradient(135deg,#d8c8a8,#e6d27a 55%,#a89a80)" role="img" aria-label="Photograph of an elderly couple at a dinner table"></div>
  <div class="tile" style="left:761px;top:856px;background:linear-gradient(135deg,#9a9a9a,#d8d8d8 50%,#3a3a3a)" role="img" aria-label="Black and white photograph of an elderly couple laughing"></div>
  <div class="tile" style="left:149px;top:1228px;background:linear-gradient(135deg,#e8e0d4,#d8507a 50%,#6a8a50)" role="img" aria-label="Photograph of pink roses on a table"></div>
  <div class="tile" style="left:455px;top:1228px;background:linear-gradient(135deg,#5a5050,#c8b8b0 55%,#e8e8e8)" role="img" aria-label="Photograph of an elderly woman looking out a window"></div>
  <div class="tile" style="left:761px;top:1228px;background:linear-gradient(135deg,#a8a8a0,#c0c8b0 50%,#8a9a70)" role="img" aria-label="Photograph of a grandmother with two grandchildren"></div>

  <div class="tile-caption" style="left:149px;top:1160px">Nique Porro Quisquam</div>
  <div class="tile-meta" style="left:149px;top:1187px">APPL ICONS, UI</div>
  <div class="tile-caption" style="left:455px;top:1160px">Nique Porro Quisquam</div>
  <div class="tile-meta" style="left:455px;top:1187px">APPL ICONS, UI</div>
  <div class="tile-caption" style="left:761px;top:1160px">Nique Porro Quisquam</div>
  <div class="tile-meta" style="left:761px;top:1187px">APPL ICONS, UI</div>
  <div class="tile-caption" style="left:149px;top:1531px">Nique Porro Quisquam</div>
  <div class="tile-meta" style="left:149px;top:1558px">APPL ICONS, UI</div>
  <div class="tile-caption" style="left:455px;top:1531px">Nique Porro Quisquam</div>
  <div class="tile-meta" style="left:455px;top:1558px">APPL ICONS, UI</div>
  <div class="tile-caption" style="left:761px;top:1531px">Nique Porro Quisquam</div>
  <div class="tile-meta" style="left:761px;top:1558px">APPL ICONS, UI</div>

  <div class="btn btn-orange" style="left:508px;top:1611px;width:181px;height:55px">Watch more</div>
</section>

<section class="about">
  <div class="about-panel"></div>
  <div class="about-photo" role="img" aria-label="Photograph of blue grape hyacinth flowers"></div>
  <span class="heading-mark tr" style="left:396px;top:28px;border-color:#fff;opacity:.8"></span>
  <h2 class="about-title">About</h2>
  <span class="heading-mark bl" style="left:228px;top:88px;border-color:#fff;opacity:.8"></span>
  <p class="about-text">Aaliquam pretium ipsum. Pellentesque sodales ipsum et enim rutrum adipiscing. Quisque tincidunt mattis sapien, vel posuere Aliquam metus neque, bibendum sit amet porta et, consequat et nim. In ut turpis non ipsum rhoncus porttitor vel ac nunc. Maecenas interdum dignissim lorem quis auctor. Donec sit amet nulla nisl, aliquam pretium ipsum. Pellentesque sodales ipsum et enim rutrum adipiscing. Quisque tincidunt mattis sapien, vel posuere Aliquam metus neque</p>
  <div class="btn btn-orange" style="left:251px;top:388px;width:179px;height:55px">Learn more</div>
  <div class="video">
    <div class="video-frame" role="img" aria-label="Video still of people lighting candles at a memorial vigil"></div>
    <div class="video-bar">
      <svg width="512" height="26" viewBox="0 0 512 26">
        <rect x="8" y="8" width="3" height="10" fill="#fff"/><rect x="14" y="8" width="3" height="10" fill="#fff"/>
        <text x="28" y="17" font-size="10" fill="#ddd" font-family="Roboto,sans-serif">00:00/00:00</text>
        <rect x="100" y="11" width="350" height="4" rx="2" fill="#777"/>
        <circle cx="104" cy="13" r="5" fill="#fff"/>
        <rect x="458" y="7" width="22" height="12" fill="#555"/>
        <path d="M490 10 h4 l5 -4 v14 l-5 -4 h-4z" fill="#fff"/>
      </svg>
    </div>
  </div>
</section>

<section class="testimonials">
  <span class="heading-mark tr" style="left:768px;top:38px"></span>
  <h2 class="heading" style="top:64px;font-family:'Cinzel',Georgia,serif">Testimonials</h2>
  <span class="heading-mark bl" style="left:408px;top:102px"></span>
  <div class="avatar" role="img" aria-label="Portrait photograph of the person giving the testimonial"></div>
  <p class="quote">“Fusce dapibus, tellus ac cursus commodo, tortor mauris condimentum. Duis mollis, est non commodo luctus, nisi erat ”</p>
  <div class="quote-name">Marten Holloway, Riverside Trust</div>
  <div class="dots"><span></span><span></span><span class="on"></span><span></span><span></span><span></span></div>
</section>

<section class="contact">
  <span class="heading-mark tr" style="left:768px;top:2748px"></span>
  <h2 class="heading" style="top:2768px">Leave a message</h2>
  <span class="heading-mark bl" style="left:408px;top:2818px"></span>
  <div class="field" style="top:2894px;height:61px">Your Name</div>
  <div class="field" style="top:2982px;height:61px">Your Email</div>
  <div class="field area" style="top:3071px;height:225px">Your Message</div>
  <div class="btn btn-orange" style="left:153px;top:3326px;width:179px;height:55px">Send email</div>

  <p class="contact-text">Lorem ipsum dolor sit amet, consectetuer adipiscing elit. Donec odio. Quisque volutpat mattis eros. Nullam malesuada erat ut turpis. Suspendisse urna nibh, viverra non, semper suscipit, posuere a, pede.</p>
  <p class="contact-addr" style="top:3028px">48 Larkfield Row, Camden,<br>London NW1 7QE, United Kingdom.</p>
  <p class="contact-addr" style="top:3121px">T: (020) 555-0142<br>M: (020) 555-0187</p>
  <span class="social" style="left:636px" aria-label="Social link"></span>
  <span class="social" style="left:727px" aria-label="Social link"></span>
  <span class="social" style="left:820px" aria-label="Social link"></span>
</section>

<footer class="site-footer">© 2016 All rights reserved</footer>

</body>
</html>
```